Business Cards for Demolition & Salvage Company

We are Licensed Demolition Contractors and this business card design is for our Salvage Yard. We recycle over 95% of the building materials removed from each demolition site in which we take to our Salvage Yard for resale eg. bricks, windows, doors, kitchens, stoves, lights, fencing etc so pretty much everything.
Updates

I forgot to note that single sided business card only please.

Reason: I would like to ask if designers could please submit or re-submit their designs edited to a single sided card only. The card also does not need space for an employee name or position as our general business contact details will suffice for this project. Primary colour must be ROYAL BLUE with no exceptions please. Much appreciated and thank you to all whom have submitted designs to date and I look forward to receiving your edited designs..

Industry/Entity Type

Building

Contact Information for Business Card

Tolvanek Demolition & Salvage (WA) Pty Ltd
2317 Carrowby Ridge Road
LOWER MIRRABEL WA 6182
P: (08) 9473 5068
F: (08) 9473 2257
E: salvage@tkwreck.com.au
W: tolvanekdemolition.com.au

Requirements
Must have
• We have a logo that has been with our Company since 1974 so he must be included in the design - file attached. As for colours, we have always used royal blue and again this must be the primary colour used in the design. Please keep the design simple.
Nice to have
• Card can include opening hours as follows:
Opening Hours:
Monday to Friday 8am - 5.00pm
Saturday 8am - 3pm
Closed Sunday's and public holidays

```html
<!DOCTYPE html>
<html lang="en">
<head>
<meta charset="utf-8">
<title>Tolvanek Demolition &amp; Salvage – Business Card</title>
<link rel="stylesheet" href="https://fonts.googleapis.com/css2?family=Open+Sans:wght@400;600;700&display=swap">
<style>
  :root {
    --royal-blue: #0b55a6;
    --sky-blue: #2c9ed8;
    --fold-navy: #0a2f5c;
    --card-white: #ffffff;
    --ink: #1a1a1a;
    --page-bg: #e6e7e9;
  }
  * { margin: 0; padding: 0; box-sizing: border-box; }
  html, body { width: 1200px; height: 900px; overflow: hidden; }
  body {
    background: var(--page-bg);
    font-family: "Open Sans", Arial, sans-serif;
    position: relative;
  }
  .card {
    position: absolute;
    left: 100px; top: 164px;
    width: 1000px; height: 572px;
    background: var(--card-white);
    box-shadow: 0 10px 30px rgba(0,0,0,0.18);
    overflow: hidden;
  }
  .card__contact-panel {
    position: absolute;
    left: 440px; top: 0;
    width: 560px; height: 100%;
    background: var(--royal-blue);
  }
  .brand {
    position: absolute;
    left: 0; top: 120px;
    width: 440px;
    display: flex; align-items: center; justify-content: center; gap: 14px;
  }
  .brand__dot {
    width: 34px; height: 34px; border-radius: 50%;
    background: var(--royal-blue);
  }
  .brand__name {
    font-size: 52px; font-weight: 700; color: var(--royal-blue);
    letter-spacing: 1px;
  }
  .hours {
    position: absolute;
    left: 0; top: 410px; width: 440px;
    text-align: center; color: var(--ink);
  }
  .hours__title {
    display: inline-block;
    background: var(--sky-blue); color: #fff;
    font-size: 24px; font-weight: 600;
    padding: 2px 14px; margin-bottom: 10px;
  }
  .hours__line { font-size: 23px; font-weight: 700; line-height: 33px; }
  .name-banner {
    position: absolute;
    left: 415px; top: 110px;
    width: 585px; height: 100px;
    background: var(--sky-blue);
    color: #fff;
    padding: 14px 0 0 48px;
    font-size: 27px; font-weight: 600; line-height: 36px;
    text-transform: uppercase; letter-spacing: 0.5px;
  }
  .name-banner__fold {
    position: absolute; left: 415px; top: 210px;
  }
  .contacts {
    position: absolute;
    left: 478px; top: 262px;
    color: #fff; font-size: 25px; line-height: 38px;
    list-style: none;
  }
  .contacts__label { display: inline-block; width: 24px; font-weight: 700; }
  .address {
    position: absolute;
    left: 478px; top: 430px;
    color: #fff; font-size: 25px; line-height: 36px;
  }
</style>
</head>
<body>
  <section class="card" aria-label="Business card">
    <div class="card__contact-panel"></div>

    <div class="brand">
      <span class="brand__dot"></span>
      <span class="brand__name">Tolvanek</span>
    </div>

    <div class="hours">
      <span class="hours__title">OPENING HOURS</span>
      <p class="hours__line">Monday to Friday 8am - 5.00pm</p>
      <p class="hours__line">Saturday 8am - 3pm</p>
      <p class="hours__line">Closed Sunday's &amp; public holidays</p>
    </div>

    <h1 class="name-banner">Tolvanek Demolition<br>&amp; Salvage (WA) Pty Ltd</h1>
    <svg class="name-banner__fold" width="25" height="16" viewBox="0 0 25 16">
      <polygon points="0,0 25,0 25,16" fill="var(--fold-navy)"/>
    </svg>

    <ul class="contacts">
      <li><span class="contacts__label">P</span>: (08) 9473 5068</li>
      <li><span class="contacts__label">F</span>: (08) 9473 2257</li>
      <li><span class="contacts__label">E</span>: salvage@tkwreck.com.au</li>
      <li><span class="contacts__label">W</span>: tolvanekdemolition.com.au</li>
    </ul>

    <address class="address" style="font-style:normal">
      2317 Carrowby Ridge Road<br>
      LOWER MIRRABEL WA&nbsp;&nbsp;6182
    </address>
  </section>
</body>
</html>
```